Norwegian psychologist service needs a fresh and exiting web site*

Norwegian psychologist service: working with therapy, personal development, mastery and personal growth. Focus: children and teenagers with special needs; family dynamics; group processes; individuals with a need for therapy and personal growth. (Our company name: Fjordlys og samhold (means Mastery and Growth).

We already have a logo for the company, which will be used (will be attached in the project).

The webside is to be structured in 4 pages with roll down curtain menus (the numbers are just for guiding the designer - the should not be added):

Page 1: Om Fjordlys og Samhold (about Mastery and Growth): this is where our business is is presented/described shortly: Lorem Ipsum dolor cit...

Page 2: Tjenester (Services): this is where our 5 service areas are presented:
2.1 Utredning (Investigation, diagnosing): Lorem Ipsum dolor cit...
2.2 Rådgivning (consulting): Lorem Ipsum dolor cit...

2.3 Kurs og work shops (courses and work shops): Lorem Ipsum dolor cit...
2.3a Fjordlys og samhold Tema 1 (T1)
2.3b Fjordlys og samhold Tema 2 (T2)
2.3c Fjordlys og samhold Tema 3 (T3)

2.4 Terapi og utvikling (Therapy and development)
2.4a Fjordlys og samhold for individer (FS1)
2.4b Fjordlys og samhold i familier (FS2)
2.4c Fjordlys og samhold i grupper (FS3)
2.4d Fjordlys og samhold i institusjoner (FS4)

Page 3: Aktuelt (Blog): this is our blog where we share knowledge and articles

Page 4: Kontakt (Contact): This is the contact form page. Contact form should constitute:
- Ditt navn (your name)
- E-post (your e-mail)
- Emne (subject)
- Melding (message/description)

Our project should also include suggestion for handheld units (iPhone, iPad).
Updates

We have both been traveling with work for a while, and then unfortunately both of us got sick on return, so we need a few more days to evaluate and choose design. Kind Regards Arvid & Margit

Target Market(s)

Focus on therapy, learning, mastery and growth for children and teenagers with special needs, within the family dynamics, or in a group setting.
OUR MARKETS:
Private market: individuals, families, groups and health industry institutions (with focus on learning, mastery, growth (as well as growing up) and psychiatry for children and teenagers with special difficulties and needs)
Public institutions: Government institutions, state institutions and municipality institutions (e.g. schools, municipality health service, hospitals) that serve the public (families with children and teenagers with special needs, and where learning, mastery, growth (as well as growing up) and potential psychiatry is an issue).

Number of Pages Required

4 page

Font styles to use
Sans Serif

Colors

Designer to choose colors to be used in the design.

Requirements
Must have
• The website must have 4 pages with roll down curtain menus (we have added a PDF with suggested structure, and headings, with sub menus - see attached PDF drawing.
• The web page must also use the added logo file - and make the web page work well with our logo.
• We would like the website to have a modern look and we would like the site to be associated with typical HIGH END TOP QUALITY private health institutions, but with a stronger focus on human beings (hands, faces etc), and not white coats and doctors. We are psychologists in the private market.
• For instance, if photos are being used - we tend to like "warm" almost art-like, "grainy" two-tone (e.g. sepia) photos to illustrate our focus. If designer can find such photos as part of design, it would be interesting to us. We would like a few photos like that integrated in the design.
• We also want a design suggestion for how the web page should look like and behave on handheld units (e.g. iPhone, iPad).
Nice to have
• If designer could find a number of suitable photos that matches the business idea and design requirements (see description above), that could follow website, that would be good.
• It could also be nice to have graphic symbols that denote the different pages/subpages (subjects)....
• HORSES: we sometimes use horses as a "tool" in therapy sessions. The horse is not necessarily used for riding, but for contact, communication and grooming. PHOTOS: we would like the designer to find an opportunity for using a photo reflecting this cooperation between therapist, child, teenager and horse. It is a bit up to the designer to find a way to do this... Since the horse is only a tool, among many other tools, it does not have to be much - but we want to try and see how it will work with a photo that also reflects this part of our business.

```html
<!DOCTYPE html>
<html lang="en">
<head>
<meta charset="utf-8">
<title>Fjordlys og Samhold — Website Design</title>
<link href="https://fonts.googleapis.com/css2?family=Open+Sans:wght@400;600;700&family=Roboto:wght@400;500&display=swap" rel="stylesheet">
<style>
:root{
  --board:#e6e6e6;
  --navy:#2c3a97;
  --navy-deep:#283593;
  --ink:#1d1d1d;
  --body:#5c5c5c;
  --orange:#ff6a00;
  --panel:#f4f4f4;
  --line:#e2e2e2;
  --white:#ffffff;
  --photo-a:#4e4e4e;
  --photo-b:#a8a8a8;
}
*{box-sizing:border-box;margin:0;padding:0}
html,body{width:877px;height:1200px;overflow:hidden;background:var(--board)}
.board{position:relative;width:877px;height:1200px;background:var(--board);font-family:"Roboto",Arial,sans-serif;overflow:hidden}
.brand-mark{position:absolute;left:0;top:118px;width:877px;text-align:center;font-family:"Open Sans",Arial,sans-serif;font-weight:600;color:var(--navy);font-size:34px;letter-spacing:1px}
.brand-dot{position:absolute;left:418px;top:52px;width:42px;height:42px;border-radius:50%;background:var(--navy)}

.site{position:absolute;top:222px;width:314px;height:934px;background:var(--white);box-shadow:0 4px 14px rgba(0,0,0,.12);overflow:hidden}
.site.left{left:78px}
.site.right{left:465px}
.site .a{position:absolute}
.h{font-family:"Open Sans",Arial,sans-serif;font-weight:600;color:var(--ink);text-transform:uppercase}

.topbar{left:0;top:0;width:314px;height:11px;background:var(--navy)}
.tb-text{top:2.6px;font-size:4.4px;color:var(--white);font-weight:500;white-space:nowrap;display:flex;align-items:center;gap:2px}
.social{top:2px;display:flex;gap:3.5px}
.social i{display:block;width:7px;height:7px;border-radius:50%;border:0.8px solid var(--white)}

.navlogo{left:24px;top:4px;width:50px;height:50px;border-radius:50%;background:var(--white);z-index:3;display:flex;align-items:flex-end;justify-content:center;padding-bottom:14px}
.navlogo span{font-family:"Open Sans",Arial,sans-serif;font-weight:600;color:var(--navy);font-size:4.3px;text-align:center;line-height:1.1}
.nav{top:20px;font-family:"Open Sans",Arial,sans-serif;font-weight:600;font-size:4.1px;color:var(--ink);white-space:nowrap}
.nav.active{color:var(--navy);text-decoration:underline}

.hero{left:0;top:34px;width:314px;height:152px;background:linear-gradient(100deg,var(--photo-a),#8a8a8a 45%,#6d6d6d 70%,var(--photo-b))}
.hero-title{left:0;top:87px;width:314px;text-align:center;font-size:14.5px;color:var(--white);font-weight:600;z-index:2}
.hero-sub{left:60px;top:104px;width:194px;text-align:center;font-size:5.6px;line-height:8.3px;color:var(--white);z-index:2}
.btn{background:var(--orange);color:var(--white);font-family:"Open Sans",Arial,sans-serif;font-weight:600;text-align:center;text-transform:uppercase}
.hero-btn{left:128px;top:126px;width:58px;height:17px;font-size:6.4px;line-height:17px;z-index:2}

.dropdown{left:177px;top:33px;width:79px;height:33px;background:var(--white);box-shadow:0 2px 5px rgba(0,0,0,.2);z-index:4;padding:3px 0 0 4px}
.dropdown li{list-style:none;font-family:"Open Sans",Arial,sans-serif;font-weight:600;font-size:3.9px;color:var(--ink);line-height:6.8px;display:flex;align-items:center;gap:2px}
.dropdown li::before{content:"";width:3px;height:2px;border-radius:50% 0;background:var(--navy);transform:rotate(-30deg)}

.about-title{left:24px;top:229px;font-size:10px}
.para{font-size:3.9px;line-height:8.9px;color:var(--body);text-align:justify}
.about-text{left:24px;top:241px;width:124px}
.photo{background:linear-gradient(135deg,#cfcfcf,#8d8d8d 55%,#bdbdbd)}
.about-photo1{left:191px;top:210px;width:100px;height:90px}
.about-photo2{left:161px;top:260px;width:84px;height:51px;border:1.5px solid var(--white)}

.svc-title{left:0;top:334px;width:314px;text-align:center;font-size:11px}
.svc-sub{left:62px;top:351px;width:190px;text-align:center;font-size:4.2px;line-height:7px;color:var(--body)}
.card{top:376px;width:61px;height:64px;background:var(--white);box-shadow:0 1px 4px rgba(0,0,0,.13);text-align:center}
.card.hover{box-shadow:0 2px 8px rgba(44,58,151,.3)}
.card-icon{position:absolute;left:19px;top:3px;width:22px;height:20px;border-radius:3px;background:linear-gradient(135deg,#fde1cc,#dfe2f3)}
.card-title{position:absolute;left:2px;top:27px;width:57px;height:12px;display:flex;align-items:center;justify-content:center;font-family:"Open Sans",Arial,sans-serif;font-weight:600;font-size:4.8px;line-height:6.6px;color:var(--navy-deep);text-transform:uppercase}
.card-text{position:absolute;left:3px;top:41px;width:55px;font-size:3.3px;line-height:5.5px;color:var(--body);text-align:justify}
.learn{position:absolute;left:0;top:54px;width:61px;text-align:center;font-family:"Open Sans",Arial,sans-serif;font-weight:600;font-size:3.7px;color:var(--orange)}

.blog-band{left:0;top:465px;width:314px;height:170px;background:var(--panel)}
.blog-title{left:0;top:476px;width:314px;text-align:center;font-size:11px}
.post{top:498px;width:78px}
.post-img{position:relative;width:78px;height:70px;background:linear-gradient(150deg,#bdbdbd,#6e6e6e 60%,#9c9c9c)}
.date{position:absolute;left:22px;bottom:0;width:34px;height:6px;font-size:3.3px;line-height:6px;color:var(--white);background:var(--orange);text-align:center;font-family:"Open Sans",Arial,sans-serif;font-weight:600}
.post-title{margin-top:5px;font-family:"Open Sans",Arial,sans-serif;font-weight:600;font-size:5.8px;color:var(--navy-deep);text-transform:uppercase;white-space:nowrap}
.post-text{margin-top:4px;font-size:3.4px;line-height:6.7px;color:var(--body);text-align:justify}
.read{margin-top:5px;font-family:"Open Sans",Arial,sans-serif;font-weight:600;font-size:3.6px;color:var(--orange);text-decoration:underline}

.contact-frame{left:23px;top:667px;width:150px;height:155px;border:0.8px solid #d5d5d5;background:var(--white)}
.contact-inner{left:30px;top:674px;width:137px;height:141px;background:var(--panel)}
.contact-title{left:30px;top:690px;width:137px;text-align:center;font-size:11px}
.field{background:var(--white);font-size:3.6px;color:#777;padding:5px 3px}
.contact-photo{left:173px;top:680px;width:117px;height:135px;background:linear-gradient(110deg,#d2d2d2,#8e8e8e 45%,#5c5c5c 75%,#a9a9a9)}
.submit{left:81px;top:801px;width:35px;height:11px;font-size:3.8px;line-height:11px}

.footer{left:0;top:843px;width:314px;height:91px;background:var(--navy)}
.f-logo{left:24px;top:858px;font-family:"Open Sans",Arial,sans-serif;font-weight:600;font-size:5.4px;color:var(--white);line-height:1.15}
.f-desc{left:24px;top:877px;width:60px;font-size:3.6px;line-height:6.2px;color:var(--white);text-align:justify}
.f-head{top:862px;font-family:"Open Sans",Arial,sans-serif;font-weight:600;font-size:5.6px;color:var(--white);text-transform:uppercase;white-space:nowrap}
.f-list{top:873px;list-style:none;font-size:3.9px;line-height:8.9px;color:var(--white);white-space:nowrap}
.f-copy{left:24px;top:924px;font-size:3.6px;color:var(--white);white-space:nowrap}
.f-social{top:922px}
</style>
</head>
<body>
<div class="board">
  <div class="brand-dot"></div>
  <div class="brand-mark">FJORDLYS OG SAMHOLD</div>

  <!-- Home page, default state -->
  <section class="site left">
    <div class="a topbar"></div>
    <div class="a tb-text" style="left:24px"><svg width="4" height="4" viewBox="0 0 10 10"><path fill="#fff" d="M2 0h2l1 3-1.5 1a6 6 0 0 0 2.5 2.5L7 5l3 1v2a2 2 0 0 1-2 2A8 8 0 0 1 0 2a2 2 0 0 1 2-2z"/></svg>40112233 (MARGIT DAHL)</div>
    <div class="a tb-text" style="left:89px"><svg width="5" height="4" viewBox="0 0 10 8"><rect x=".5" y=".5" width="9" height="7" fill="none" stroke="#fff"/><path d="M.5.5 5 4.5 9.5.5" fill="none" stroke="#fff"/></svg>Margit@fjordlysogsamhold.no</div>
    <div class="a social" style="left:252px"><i></i><i></i><i></i><i></i></div>

    <div class="a navlogo"><span>FJORDLYS<br>OG SAMHOLD</span></div>
    <div class="a nav active" style="left:141px">HOME</div>
    <div class="a nav" style="left:168px">ABOUT US</div>
    <div class="a nav" style="left:204px">SERVICES ⌄</div>
    <div class="a nav" style="left:238px">BLOG</div>
    <div class="a nav" style="left:263px">CONTACT US</div>

    <div class="a hero" role="img" aria-label="Grey-toned photo of a smiling girl talking with a therapist"></div>
    <div class="a h hero-title">FJORDLYS OG SAMHOLD</div>
    <div class="a hero-sub">Main focus on family, children, childhood and school. Children with functional difficulties and special care needs.</div>
    <div class="a btn hero-btn">GET STARTED</div>

    <div class="a h about-title">ABOUT US</div>
    <div class="a para about-text">Main focus on family, children, childhood and school. Children with functional difficulties and special care needs.Lorem ipsum dolor sit amet, consectetur adipiscing elit, sed do eiusmod tempor incididunt ut labore et dolore magna aliqua. Ut enim ad minim veniam, quis nostrud exercitation ullamco laboris nisi ut aliquip ex ea commodo consequat. Duis aute irure dolor in reprehenderit</div>
    <div class="a photo about-photo1" role="img" aria-label="Grey-toned photo of a girl in session with a therapist"></div>
    <div class="a photo about-photo2" role="img" aria-label="Grey-toned photo of a boy raising his hand"></div>

    <div class="a h svc-title">SERVICES WE PROVIDE</div>
    <div class="a svc-sub">Lorem ipsum dolor sit amet, consectetur adipiscing elit, sed do eiusmod tempor incididunt ut labore et dolore magna aliqua</div>

    <div class="a card" style="left:23px"><div class="card-icon" role="img" aria-label="Line icon of a person with a question mark"></div><div class="card-title">Investigation &amp;<br>Diagnosing</div><div class="card-text">Lorem ipsum dolor sit amet, consectetur adipiscing elit, sed do</div><div class="learn">LEARN MORE &nbsp;›</div></div>
    <div class="a card" style="left:92px"><div class="card-icon" role="img" aria-label="Line icon of a person with a speech bubble"></div><div class="card-title">Consulting</div><div class="card-text">Lorem ipsum dolor sit amet, consectetur adipiscing elit, sed do</div><div class="learn">LEARN MORE &nbsp;›</div></div>
    <div class="a card hover" style="left:161px"><div class="card-icon" role="img" aria-label="Line icon of a presenter and audience"></div><div class="card-title">Courses and<br>Workshops</div><div class="card-text">Lorem ipsum dolor sit amet, consectetur adipiscing elit, sed do</div><div class="learn">LEARN MORE &nbsp;›</div></div>
    <div class="a card" style="left:230px"><div class="card-icon" role="img" aria-label="Line icon of a horse and a child"></div><div class="card-title">Therapy and<br>Development</div><div class="card-text">Lorem ipsum dolor sit amet, consectetur adipiscing elit, sed do</div><div class="learn">LEARN MORE &nbsp;›</div></div>

    <div class="a blog-band"></div>
    <div class="a h blog-title">BLOG</div>
    <article class="a post" style="left:23px"><div class="post-img" role="img" aria-label="Grey-toned photo of a family meeting"><span class="date">JAN 20 2020</span></div><div class="post-title">Neque porro quisquam</div><div class="post-text">It is a long established fact that a reader will be distracted by the readable content of a page when looking at its layout. The point of using Lorem Ipsum is that it has.</div><div class="read">READ MORE</div></article>
    <article class="a post" style="left:117px"><div class="post-img" role="img" aria-label="Grey-toned photo of a therapist by a bookshelf"><span class="date">JAN 20 2020</span></div><div class="post-title">Dolorem ipsum quia</div><div class="post-text">It is a long established fact that a reader will be distracted by the readable content of a page when looking at its layout. The point of using Lorem Ipsum is that it has.</div><div class="read">READ MORE</div></article>
    <article class="a post" style="left:212px"><div class="post-img" role="img" aria-label="Grey-toned photo of a child drawing at a table"><span class="date">JAN 20 2020</span></div><div class="post-title">Finibus bonorum et</div><div class="post-text">Sed ut perspiciatis unde omnis iste natus error sit voluptatem accusantium doloremque laudantium, totam rem aperiam, eaque ipsa quae ab illo inventore veritatis et.</div><div class="read">READ MORE</div></article>

    <div class="a contact-frame"></div>
    <div class="a contact-inner"></div>
    <div class="a contact-photo" role="img" aria-label="Grey-toned photo of a therapist talking with a child"></div>
    <div class="a h contact-title">CONTACT US</div>
    <div class="a field" style="left:34px;top:711px;width:61px;height:16px">Name</div>
    <div class="a field" style="left:102px;top:711px;width:61px;height:16px">Email address</div>
    <div class="a field" style="left:34px;top:730px;width:129px;height:16px">Subject</div>
    <div class="a field" style="left:34px;top:749px;width:129px;height:42px">Messages</div>
    <div class="a btn submit">SUBMIT</div>

    <footer class="a footer"></footer>
    <div class="a f-logo">FJORDLYS<br>OG SAMHOLD</div>
    <div class="a f-desc">Main focus on family, children, childhood and school. Children with functional difficulties and special care needs</div>
    <div class="a f-head" style="left:104px">Quicks Links</div>
    <ul class="a f-list" style="left:104px"><li>Home</li><li>About Us</li><li>Services</li><li>Blog</li><li>Contact Us</li></ul>
    <div class="a f-head" style="left:158px">Services</div>
    <ul class="a f-list" style="left:158px"><li>Investigation &amp; Diagnosing</li><li>Consulting</li><li>Courses and Workshops</li><li>Therapy and development</li></ul>
    <div class="a f-head" style="left:232px">Contact Us</div>
    <ul class="a f-list" style="left:232px"><li>Havnegata 14,</li><li>0150 Oslo</li><li>40112233 (Margit Dahl)</li><li>Margit@fjordlysogsamhold.no</li></ul>
    <div class="a f-copy">Copyright © 2020 &nbsp;Fjordlys og samhold &nbsp;| &nbsp;Terms of Use &nbsp;| &nbsp;Privacy Policy</div>
    <div class="a social f-social" style="left:252px"><i></i><i></i><i></i><i></i></div>
  </section>

  <!-- Home page, services menu open -->
  <section class="site right">
    <div class="a topbar"></div>
    <div class="a tb-text" style="left:24px"><svg width="4" height="4" viewBox="0 0 10 10"><path fill="#fff" d="M2 0h2l1 3-1.5 1a6 6 0 0 0 2.5 2.5L7 5l3 1v2a2 2 0 0 1-2 2A8 8 0 0 1 0 2a2 2 0 0 1 2-2z"/></svg>40112233 (MARGIT DAHL)</div>
    <div class="a tb-text" style="left:89px"><svg width="5" height="4" viewBox="0 0 10 8"><rect x=".5" y=".5" width="9" height="7" fill="none" stroke="#fff"/><path d="M.5.5 5 4.5 9.5.5" fill="none" stroke="#fff"/></svg>Margit@fjordlysogsamhold.no</div>
    <div class="a social" style="left:252px"><i></i><i></i><i></i><i></i></div>

    <div class="a navlogo"><span>FJORDLYS<br>OG SAMHOLD</span></div>
    <div class="a nav" style="left:141px">HOME</div>
    <div class="a nav" style="left:168px">ABOUT US</div>
    <div class="a nav active" style="left:204px">SERVICES ⌄</div>
    <div class="a nav" style="left:238px">BLOG</div>
    <div class="a nav" style="left:263px">CONTACT US</div>

    <div class="a hero" role="img" aria-label="Grey-toned photo of a smiling girl talking with a therapist"></div>
    <ul class="a dropdown"><li>INVESTIGATION &amp; DIAGNOSING</li><li>CONSULTING</li><li>COURSES AND WORKSHOPS</li><li>THERAPY AND DEVELOPMENT</li></ul>
    <div class="a h hero-title">FJORDLYS OG SAMHOLD</div>
    <div class="a hero-sub">Main focus on family, children, childhood and school. Children with functional difficulties and special care needs.</div>
    <div class="a btn hero-btn">GET STARTED</div>

    <div class="a h about-title">ABOUT US</div>
    <div class="a para about-text">Main focus on family, children, childhood and school. Children with functional difficulties and special care needs.Lorem ipsum dolor sit amet, consectetur adipiscing elit, sed do eiusmod tempor incididunt ut labore et dolore magna aliqua. Ut enim ad minim veniam, quis nostrud exercitation ullamco laboris nisi ut aliquip ex ea commodo consequat. Duis aute irure dolor in reprehenderit</div>
    <div class="a photo about-photo1" role="img" aria-label="Grey-toned photo of a girl in session with a therapist"></div>
    <div class="a photo about-photo2" role="img" aria-label="Grey-toned photo of a boy raising his hand"></div>

    <div class="a h svc-title">SERVICES WE PROVIDE</div>
    <div class="a svc-sub">Lorem ipsum dolor sit amet, consectetur adipiscing elit, sed do eiusmod tempor incididunt ut labore et dolore magna aliqua</div>

    <div class="a card" style="left:23px"><div class="card-icon" role="img" aria-label="Line icon of a person with a question mark"></div><div class="card-title">Investigation &amp;<br>Diagnosing</div><div class="card-text">Lorem ipsum dolor sit amet, consectetur adipiscing elit, sed do</div><div class="learn">LEARN MORE &nbsp;›</div></div>
    <div class="a card" style="left:92px"><div class="card-icon" role="img" aria-label="Line icon of a person with a speech bubble"></div><div class="card-title">Consulting</div><div class="card-text">Lorem ipsum dolor sit amet, consectetur adipiscing elit, sed do</div><div class="learn">LEARN MORE &nbsp;›</div></div>
    <div class="a card hover" style="left:161px"><div class="card-icon" role="img" aria-label="Line icon of a presenter and audience"></div><div class="card-title">Courses and<br>Workshops</div><div class="card-text">Lorem ipsum dolor sit amet, consectetur adipiscing elit, sed do</div><div class="learn">LEARN MORE &nbsp;›</div></div>
    <div class="a card" style="left:230px"><div class="card-icon" role="img" aria-label="Line icon of a horse and a child"></div><div class="card-title">Therapy and<br>Development</div><div class="card-text">Lorem ipsum dolor sit amet, consectetur adipiscing elit, sed do</div><div class="learn">LEARN MORE &nbsp;›</div></div>

    <div class="a blog-band"></div>
    <div class="a h blog-title">BLOG</div>
    <article class="a post" style="left:23px"><div class="post-img" role="img" aria-label="Grey-toned photo of a family meeting"><span class="date">JAN 20 2020</span></div><div class="post-title">Neque porro quisquam</div><div class="post-text">It is a long established fact that a reader will be distracted by the readable content of a page when looking at its layout. The point of using Lorem Ipsum is that it has.</div><div class="read">READ MORE</div></article>
    <article class="a post" style="left:117px"><div class="post-img" role="img" aria-label="Grey-toned photo of a therapist by a bookshelf"><span class="date">JAN 20 2020</span></div><div class="post-title">Dolorem ipsum quia</div><div class="post-text">It is a long established fact that a reader will be distracted by the readable content of a page when looking at its layout. The point of using Lorem Ipsum is that it has.</div><div class="read">READ MORE</div></article>
    <article class="a post" style="left:212px"><div class="post-img" role="img" aria-label="Grey-toned photo of a child drawing at a table"><span class="date">JAN 20 2020</span></div><div class="post-title">Finibus bonorum et</div><div class="post-text">Sed ut perspiciatis unde omnis iste natus error sit voluptatem accusantium doloremque laudantium, totam rem aperiam, eaque ipsa quae ab illo inventore veritatis et.</div><div class="read">READ MORE</div></article>

    <div class="a contact-frame"></div>
    <div class="a contact-inner"></div>
    <div class="a contact-photo" role="img" aria-label="Grey-toned photo of a therapist talking with a child"></div>
    <div class="a h contact-title">CONTACT US</div>
    <div class="a field" style="left:34px;top:711px;width:61px;height:16px">Name</div>
    <div class="a field" style="left:102px;top:711px;width:61px;height:16px">Email address</div>
    <div class="a field" style="left:34px;top:730px;width:129px;height:16px">Subject</div>
    <div class="a field" style="left:34px;top:749px;width:129px;height:42px">Messages</div>
    <div class="a btn submit">SUBMIT</div>

    <footer class="a footer"></footer>
    <div class="a f-logo">FJORDLYS<br>OG SAMHOLD</div>
    <div class="a f-desc">Main focus on family, children, childhood and school. Children with functional difficulties and special care needs</div>
    <div class="a f-head" style="left:104px">Quicks Links</div>
    <ul class="a f-list" style="left:104px"><li>Home</li><li>About Us</li><li>Services</li><li>Blog</li><li>Contact Us</li></ul>
    <div class="a f-head" style="left:158px">Services</div>
    <ul class="a f-list" style="left:158px"><li>Investigation &amp; Diagnosing</li><li>Consulting</li><li>Courses and Workshops</li><li>Therapy and development</li></ul>
    <div class="a f-head" style="left:232px">Contact Us</div>
    <ul class="a f-list" style="left:232px"><li>Havnegata 14,</li><li>0150 Oslo</li><li>40112233 (Margit Dahl)</li><li>Margit@fjordlysogsamhold.no</li></ul>
    <div class="a f-copy">Copyright © 2020 &nbsp;Fjordlys og samhold &nbsp;| &nbsp;Terms of Use &nbsp;| &nbsp;Privacy Policy</div>
    <div class="a social f-social" style="left:252px"><i></i><i></i><i></i><i></i></div>
  </section>
</div>
</body>
</html>
```